MORLIVEX Hemp based Pet Brand that growns it's own premium hemp and creates amazing pet products.

We need packaging designed for a new company based in South West Florida. We grow our own hemp with our other company Crest 4 Vale and use the harvest to make our hemp based pet products. Our initial products are pet treats that include Soft Chews and Calming Chews. The bags come in two different sizes. Regular bag being 7x10.25 inches and Small bag 4.25X6.25 inches. We also need a tincture box and label created. We want packaging that will catch the eye of the consumer and colors that compliment our logo. Dropper label size is 4x1.75 inches and the milligram of CBD is 1500. We have attached our manufacturers packaging and would like you to coppy everything other than their overall design and logo. Use default UPC and QR code, which we can replace later in the Ai file. Please see all the attached documents and please ask me if you have any questions. The final design should communicate a premium product that stand our from the rest. Something that catches the eye of the consumer by its premium appearance. Packaging is everything so I hope you can use your creative skills to create something special!

Target Market(s)

Pet owners

Font styles to use
Serif
Sans Serif

Colors
0054AA
0677BA
7BADD7
CADEEF
E8F1F8
0094D4
00A9DD
6FCCEA
C7EBF8
E9F6FB
EE7325
F08F49
F5BC92
FAE3D3
FDF4ED

Requirements
Must have
• Stand out design. Premium feel. Imagine shopping for something for your pet and seeing a brand that POPS and just looks like a good product because the packaging is so good.
Nice to have
• Modern mature feel
Should not have
• Cartoony feeling. Do not use baby blue everywhere. Do not include pictures of people in the packaging

```html
<!DOCTYPE html>
<html lang="en">
<head>
<meta charset="utf-8">
<title>MORLIVEX Calming Chews – Dropper Label</title>
<link rel="stylesheet" href="https://fonts.googleapis.com/css2?family=Archivo+Narrow:wght@700&family=Oswald:wght@500&family=Poppins:wght@400;500&display=swap">
<style>
  :root {
    --page: #ffffff;
    --navy: #0054AA;
    --blue: #0677BA;
    --blue-bright: #0094D4;
    --ice: #E9F6FB;
    --panel: #FDF4ED;
    --orange: #EE7325;
    --orange-mid: #F08F49;
    --orange-soft: #F5BC92;
    --ink: #1b1b1b;
    --white: #ffffff;
    --leaf: #1f7a3a;
  }
  * { box-sizing: border-box; margin: 0; padding: 0; }
  html, body { width: 1200px; height: 1200px; overflow: hidden; background: var(--page); }
  .canvas { position: relative; width: 1200px; height: 1200px; }

  /* 4 x 1.75 in dropper label */
  .label {
    position: absolute; left: 40px; top: 355px; width: 1120px; height: 490px;
    background: linear-gradient(90deg, var(--navy) 0%, var(--blue) 65%, var(--blue-bright) 100%);
    overflow: hidden;
  }

  .brand-mark {
    position: absolute; left: 60px; top: 110px; width: 210px; height: 210px;
    border-radius: 50%; background: var(--white);
    display: flex; align-items: center; justify-content: center;
  }
  .brand-name {
    font-family: "Archivo Narrow", sans-serif; font-weight: 700;
    font-size: 34px; letter-spacing: 3px; color: var(--navy);
  }

  .product-title {
    position: absolute; left: 310px; top: 110px; width: 480px;
    font-family: "Archivo Narrow", sans-serif; font-weight: 700;
    font-size: 72px; line-height: 1; color: var(--white); letter-spacing: -1px;
    white-space: nowrap;
  }
  .strength {
    position: absolute; left: 310px; top: 212px;
    font-family: "Oswald", sans-serif; font-weight: 500;
    font-size: 60px; line-height: 1; color: var(--orange-soft); letter-spacing: 1px;
  }
  .strength-unit { font-size: 34px; color: var(--white); letter-spacing: 2px; }

  .pet-panel {
    position: absolute; left: 815px; top: 36px; width: 270px; height: 384px;
    background: var(--panel); border: 4px solid var(--orange);
    border-bottom: none; border-radius: 135px 135px 0 0;
  }
  .leaf-icon {
    position: absolute; left: 915px; top: 80px; width: 70px; height: 64px;
    background: var(--leaf); border-radius: 50% 50% 40% 40%;
  }
  .claim {
    position: absolute; left: 815px; width: 270px; top: 168px; text-align: center;
    font-family: "Oswald", sans-serif; font-weight: 500;
    font-size: 52px; line-height: 1; color: var(--orange);
  }
  .claim-sub {
    position: absolute; left: 815px; width: 270px; top: 232px; text-align: center;
    font-family: "Poppins", sans-serif; font-weight: 400;
    font-size: 18px; letter-spacing: 3px; color: #444444;
  }
  .net-weight {
    position: absolute; left: 815px; width: 270px; top: 370px; text-align: center;
    font-family: "Poppins", sans-serif; font-size: 14px; color: var(--ink);
  }

  .base-band {
    position: absolute; left: 0; right: 0; bottom: 0; height: 70px;
    background: linear-gradient(90deg, var(--orange) 0%, var(--orange-mid) 60%, var(--orange-soft) 100%);
  }
</style>
</head>
<body>
<div class="canvas">
  <section class="label">
    <div class="brand-mark"><span class="brand-name">MORLIVEX</span></div>

    <h1 class="product-title">CALMING CHEWS</h1>
    <p class="strength">1500<span class="strength-unit">MG CBD</span></p>

    <div class="pet-panel" role="img" aria-label="Light silhouette of a dog and cat with orange outline"></div>
    <div class="leaf-icon" role="img" aria-label="Green hemp leaf icon"></div>
    <p class="claim">CBD HEMP</p>
    <p class="claim-sub">Treatment</p>
    <p class="net-weight">Net WT. 10.5 oz</p>

    <div class="base-band"></div>
  </section>
</div>
</body>
</html>
```